I am a surgeon that operates on gynaecological cancer. Wish a design and logo for letter head.

Design should include my name: Dr. Torin Halwell, qualifications: FKMLTPVB, DMR. and state that I am a Gynaecological Oncologist and Advanced Laparoscopic Surgeon.
As for a logo. As all cancer is related to DNA, I think that that double helix could be used to symbolise a female shape, exaggerating the abdomen to suggest a mass.

Reason: Extended to view changes I have asked for.

```html
<!DOCTYPE html>
<html lang="en">
<head>
<meta charset="utf-8">
<title>Dr. Torin Halwell — Letterhead</title>
<link rel="stylesheet" href="https://fonts.googleapis.com/css2?family=Montserrat:wght@500;600&family=Arimo:wght@400;700&family=Tinos&display=swap">
<style>
  :root {
    --backdrop: #e9e9e9;
    --paper: #fbfbfb;
    --navy: #1f2d5c;
    --orange: #f07d1a;
    --ink: #4a4a4a;
    --ink-soft: #6d6d6d;
  }
  * { box-sizing: border-box; margin: 0; padding: 0; }
  html, body {
    width: 1200px; height: 795px; overflow: hidden;
    background: var(--backdrop);
  }
  .canvas {
    width: 1200px; height: 795px;
    display: flex; align-items: center; justify-content: center;
  }
  .letterhead {
    position: relative;
    width: 520px; height: 735px;
    background: var(--paper);
    box-shadow: 0 6px 22px rgba(0,0,0,.12);
    font-family: "Arimo", Arial, sans-serif;
    color: var(--ink);
    overflow: hidden;
  }
  .brand {
    position: absolute; left: 44px; top: 52px;
    display: flex; align-items: center; gap: 8px;
  }
  .brand-dot {
    width: 12px; height: 12px; border-radius: 50%;
    background: var(--orange);
  }
  .brand-name {
    font-family: "Montserrat", sans-serif; font-weight: 600;
    font-size: 13px; letter-spacing: 1.2px; color: var(--navy);
  }
  .brand-tagline {
    position: absolute; left: 44px; top: 74px;
    font-family: "Montserrat", sans-serif; font-weight: 500;
    font-size: 5.5px; letter-spacing: .6px; text-transform: uppercase;
    color: var(--navy);
  }
  .sender {
    position: absolute; right: 44px; top: 50px;
    text-align: right; font-family: "Montserrat", sans-serif;
    font-style: normal; font-weight: 500;
    font-size: 6.5px; line-height: 1.55; letter-spacing: .5px;
    color: var(--ink-soft);
  }
  .sender-name { color: var(--orange); font-weight: 600; font-size: 7px; letter-spacing: 1px; margin-bottom: 2px; }
  .sender-accent { color: var(--orange); }
  .body {
    position: absolute; left: 44px; right: 110px; top: 200px;
    font-size: 8.2px; line-height: 1.45;
  }
  .body-heading { font-weight: 700; font-size: 8.6px; margin-bottom: 12px; }
  .body p { margin-bottom: 11px; }
  .signature { position: absolute; left: 44px; top: 560px; }
  .signature-name {
    font-family: "Montserrat", sans-serif; font-weight: 600;
    font-size: 7px; letter-spacing: 1px; color: var(--orange);
  }
  .signature-line {
    font-family: "Tinos", "Times New Roman", serif;
    font-size: 26px; color: var(--ink-soft); margin-top: 2px;
  }
  .footer-band {
    position: absolute; left: 0; bottom: 0; width: 100%; height: 10px;
  }
</style>
</head>
<body>
<main class="canvas">
  <article class="letterhead">
    <header>
      <div class="brand">
        <span class="brand-dot"></span>
        <span class="brand-name">DR. TORIN HALWELL</span>
      </div>
      <div class="brand-tagline">Gynaecological Oncologist and Laparoscopic Surgeon</div>

      <address class="sender">
        <div class="sender-name">DR. TORIN HALWELL</div>
        <div>Gynaecological Oncologist</div>
        <div>and Advanced Laparoscopic Surgeon</div>
        <div class="sender-accent">Consultant Surgeon</div>
        <div>FKMLTPVB, DMR</div>
      </address>
    </header>

    <section class="body">
      <h2 class="body-heading">Lorem Ipsum</h2>
      <p>Lorem Ipsum is simply dummy text of the printing and typesetting industry. Lorem Ipsum has been the industry's standard dummy text ever since the 1500s, when an unknown printer took a galley of type and scrambled it to make a type specimen book. It has survived not only five centuries, but also the leap into electronic typesetting, remaining essentially unchanged. It was popularised in the 1960s with the release of Dravenline sheets containing Lorem Ipsum passages, and more recently with desktop publishing software like Quillset Composer including versions of Lorem Ipsum.</p>
      <p>passages, and more recently with desktop publishing software like Quillset Composer including versions of Lorem Ipsum.</p>
      <p>Lorem Ipsum is simply dummy text of the printing and typesetting industry. Lorem Ipsum has been the industry's standard dummy text ever since the 1500s, when an unknown printer took a galley of type and scrambled it to make a type specimen book.</p>
      <p>Lorem Ipsum is simply dummy text of the printing and typesetting industry. Lorem Ipsum has been the industry's standard dummy text ever since the 1500s, when an unknown printer took a galley of type and scrambled it to make a type specimen book. It has survived not only five centuries, but also the leap into electronic typesetting, remaining essentially unchanged.</p>
    </section>

    <footer class="signature">
      <div class="signature-name">DR. TORIN HALWELL</div>
      <div class="signature-line">Lorem Ipsum</div>
    </footer>

    <svg class="footer-band" viewBox="0 0 520 10" preserveAspectRatio="none" aria-hidden="true">
      <polygon points="0,0 372,0 366,10 0,10" fill="var(--navy)"/>
      <polygon points="376,0 520,0 520,10 370,10" fill="var(--orange)"/>
    </svg>
  </article>
</main>
</body>
</html>
```